Psychology practice Logo and Business card design

Still in its early development, Meridian Counselling Group provides comprehensive psychology services to a diverse range of clients in the Barossa Valley. Some details available on website - www.tallowmind-example.com.
The Barossa is a semi-rural area, famous for our wines.
At Meridian Counselling Group we work with young children, adolescents, families and adults. We will soon move into our own premises in a restored historic/heritage building in the main street of Angaston. This 1870s building was most recently a bookshop, but has previously been a grocer store and secret 'clubhouse'.
The preferred therapeutic style of our psychologist is called RFT therapy - this is in part how the name of the business was decided. We are also encouraging of clients' physical health in conjunction with their emotional health.
Updates

Thank you to those designers who have already provided early ideas.

A few extra thoughts:

- given the national psychology body is the NBT, I'm keen to avoid using that abbreviation;

- simple is best;

- I would prefer the business name to be the feature rather than my own name;

- a simple logo as part of the design would be fantastic so it can be adapted for signage etc.

Many thanks for your continued help.

Target Market(s)

broad - adults, adolescents, families.

Industry/Entity Type

Building

Contact Information for Business Card

Meridian Counselling Group
www. tallowmind-example.com

PO Box 714
Larkvale SA 5391

Delia Farrant FNBT
Psychologist
BSc, Grad Dip Ed, M Psych (Clinical)
mob: 0431 957 284
fax: 0869 413 508
email: delia@tallowmind-example.com

Requirements
Must have
• Simple logo design included.
All contact information.
Reverse side for appointment details (Next appointment: Date, Time)
Nice to have
• Something representative of hope / future focus.
Possibly a combination of modern feel with connection to heritage?
Gender neutral colours
Should not have
• abbreviation to NBT
photograph

```html
<!DOCTYPE html>
<html lang="en">
<head>
<meta charset="utf-8">
<title>Meridian Counselling Group – Business Card</title>
<link rel="stylesheet" href="https://fonts.googleapis.com/css2?family=Open+Sans:wght@400;600;700&display=swap">
<style>
  :root {
    --bg-top: #f4f4f4;
    --bg-bottom: #d6d6d6;
    --card: #ffffff;
    --panel: #dcdcdc;
    --panel-dark: #c9c9c9;
    --rule: #f7f7f7;
    --band: #bdbdbd;
    --ink: #555555;
    --icon: #777777;
    --brand-blue: #1f3f9a;
    --brand-sky: #2a9ad6;
    --caption: #9a9a9a;
  }
  * { box-sizing: border-box; margin: 0; padding: 0; }
  html, body { width: 1200px; height: 1000px; overflow: hidden; }
  body {
    background: radial-gradient(ellipse at 50% 40%, var(--bg-top), var(--bg-bottom));
    font-family: "Open Sans", Arial, sans-serif;
    color: var(--ink);
    position: relative;
  }
  .card {
    position: absolute;
    width: 560px;
    height: 320px;
    background: var(--card);
    box-shadow: 0 10px 24px rgba(0,0,0,0.18), 0 2px 4px rgba(0,0,0,0.12);
  }
  .caption {
    position: absolute;
    font-size: 30px;
    color: var(--caption);
  }

  /* Back: appointment card */
  .card--back { left: 80px; top: 90px; }
  .appointment {
    position: absolute;
    inset: 22px;
    background: var(--panel);
  }
  .appointment__title {
    background: var(--panel-dark);
    text-align: center;
    font-size: 15px;
    letter-spacing: 1px;
    padding: 4px 0;
  }
  .appointment__rules {
    position: absolute;
    left: 14px; right: 14px; top: 36px; bottom: 18px;
    background: repeating-linear-gradient(to bottom, transparent 0 18px, var(--rule) 18px 20px);
  }
  .appointment__fields {
    position: absolute;
    left: 14px; top: 37px;
    font-size: 14px;
    line-height: 20px;
  }
  .caption--back { left: 660px; top: 420px; }

  /* Front */
  .card--front { left: 560px; top: 560px; }
  .front__web {
    position: absolute;
    right: 26px; top: 22px;
    font-size: 11px;
    letter-spacing: 3.5px;
  }
  .front__brand {
    position: absolute;
    left: 30px; top: 150px;
    width: 270px;
    display: flex;
    align-items: center;
    gap: 12px;
  }
  .front__brand-mark {
    width: 34px; height: 34px;
    border-radius: 50%;
    background: var(--brand-sky);
    flex: none;
  }
  .front__brand-name {
    font-weight: 700;
    font-size: 24px;
    line-height: 27px;
    color: var(--brand-blue);
  }
  .front__band {
    position: absolute;
    left: 310px; right: 0; top: 92px; height: 82px;
    background: var(--band);
    color: #ffffff;
    padding: 10px 16px;
  }
  .front__name {
    font-weight: 700;
    font-size: 19px;
    letter-spacing: 3px;
  }
  .front__role {
    font-size: 13px;
    line-height: 17px;
    letter-spacing: 0.5px;
  }
  .front__contacts {
    position: absolute;
    left: 318px; top: 190px;
    font-size: 11.5px;
    line-height: 18px;
  }
  .contact-line { display: flex; align-items: center; gap: 4px; white-space: nowrap; }
  .contact-line svg { width: 12px; height: 12px; flex: none; }
  .contact-gap { margin-left: 8px; }
  .contact-line--email { font-weight: 600; }
  .caption--front { left: 1010px; top: 880px; }
</style>
</head>
<body>

  <section class="card card--back" aria-label="Back of card">
    <div class="appointment">
      <div class="appointment__title">Your Appointment</div>
      <div class="appointment__rules"></div>
      <div class="appointment__fields">
        <div>Patient Name:</div>
        <div>Date:</div>
        <div>Time:</div>
      </div>
    </div>
  </section>
  <div class="caption caption--back">Back</div>

  <section class="card card--front" aria-label="Front of card">
    <div class="front__web">www.tallowmind-example.com</div>

    <div class="front__brand">
      <span class="front__brand-mark"></span>
      <span class="front__brand-name">Meridian<br>Counselling Group</span>
    </div>

    <div class="front__band">
      <div class="front__name">Delia Farrant</div>
      <div class="front__role">Psychologist BA,<br>Dip Couns, M Clin Sc</div>
    </div>

    <div class="front__contacts">
      <div class="contact-line">
        <svg viewBox="0 0 12 12" aria-hidden="true"><rect x="0.5" y="2" width="11" height="8" rx="1.5" fill="var(--icon)"/><path d="M1 3 L6 7 L11 3" stroke="#fff" fill="none" stroke-width="1"/></svg>
        PO Box 714 Larkvale SA 5391
      </div>
      <div class="contact-line">
        <svg viewBox="0 0 12 12" aria-hidden="true"><rect x="0.5" y="0.5" width="11" height="11" rx="2" fill="var(--icon)"/><rect x="4" y="2" width="4" height="8" rx="1" fill="#fff"/></svg>
        0431 957 284
        <svg class="contact-gap" viewBox="0 0 12 12" aria-hidden="true"><rect x="0.5" y="0.5" width="11" height="11" rx="2" fill="var(--icon)"/><rect x="2.5" y="3" width="7" height="2" fill="#fff"/><rect x="2.5" y="6.5" width="7" height="2.5" fill="#fff"/></svg>
        0869 413 508
      </div>
      <div class="contact-line contact-line--email">email: delia@tallowmind-example.com</div>
    </div>
  </section>
  <div class="caption caption--front">Front</div>

</body>
</html>
```